Whitby's Yard & Garden Center Business Card Update

I need an updated Business card design for my Lawn and Garden Center. We do Landscaping installs, Lawn Mowing, Snow Removal and also have a Garden Center Retail Division. I uploaded a few of our previous business cards to give an idea of what we are starting with. The main goal of this update is to simplify and modernize the business card, not all of the services that are on the previous cards has to be on the new one but I would still like to highlight our main services. There is also a sample of our logo that Can be used in the design.

Industry/Entity Type

Landscaping

Contact Information for Business Card

Desmond Whitby
Desmond@Whitbysyardandgarden.example
Business (555) 208-7316
Cell (555) 391-6842

Colors

Designer to choose colors to be used in the design.

Requirements
Must have
• Services Provided :
• Landscaping
• Lawn Maintenance
• Snow Removal
• Garden Center

```html
<!DOCTYPE html>
<html lang="en">
<head>
<meta charset="utf-8">
<title>Whitby's Yard & Garden Center — Business Card</title>
<link href="https://fonts.googleapis.com/css2?family=Montserrat:wght@300;400;600;700;800&display=swap" rel="stylesheet">
<style>
  :root{
    --green:#3b5229;
    --ink:#141414;
    --paper:#f4f4f2;
    --backdrop:#dcdad5;
    --ghost:#d3d7cf;
    --white:#ffffff;
  }
  *{box-sizing:border-box;margin:0;padding:0}
  html,body{width:1200px;height:843px;overflow:hidden}
  body{
    background:var(--backdrop);
    font-family:'Montserrat',sans-serif;
    color:var(--ink);
    display:flex;flex-direction:column;align-items:center;justify-content:center;gap:40px;
  }
  .card{
    position:relative;width:640px;height:366px;background:var(--paper);
    box-shadow:0 6px 18px rgba(0,0,0,.18);
  }
  .card::before{
    content:"";position:absolute;inset:12px;border:2px solid var(--ink);pointer-events:none;
  }
  .abs{position:absolute}
  .pill{
    position:absolute;height:34px;border-radius:17px;background:var(--green);color:var(--white);
    display:flex;align-items:center;justify-content:center;
    font-weight:700;font-size:15px;letter-spacing:.5px;text-transform:uppercase;
  }
  .rule{position:absolute;height:1.5px;background:var(--ink)}

  /* front */
  .brand{left:0;right:0;top:38px;display:flex;justify-content:center;align-items:center;gap:12px}
  .brand-dot{width:40px;height:40px;border-radius:50%;background:var(--green)}
  .brand-name{font-size:34px;font-weight:800;color:var(--green)}
  .front-title{left:0;right:0;top:120px;text-align:center;font-weight:800;font-size:38px;letter-spacing:1px;line-height:1}
  .front-and{left:0;right:0;top:164px;text-align:center;font-size:12px;font-weight:600;letter-spacing:1px}
  .front-sub{left:0;right:0;top:180px;text-align:center;font-weight:800;font-size:27px;letter-spacing:1px;line-height:1}

  /* back */
  .person{left:48px;top:48px;font-size:30px;letter-spacing:1px;line-height:1}
  .person b{font-weight:800}
  .person span{font-weight:300}
  .role{left:52px;top:96px;font-size:13px;letter-spacing:1px}
  .ghost{left:150px;top:118px;font-size:92px;font-weight:800;color:var(--ghost)}
  .service{
    height:28px;border-radius:14px;font-weight:300;font-size:14px;letter-spacing:1px;
    justify-content:flex-start;padding-left:28px;
  }
  .service svg{position:absolute;right:3px;top:3px}
  .company{right:50px;top:222px;text-align:right;line-height:1.15}
  .company .main{font-weight:800;font-size:14px;letter-spacing:1px}
  .company .and{font-size:7px;font-weight:600;letter-spacing:.5px}
  .company .sub{font-weight:800;font-size:10px;letter-spacing:1px;padding-bottom:3px;border-bottom:1.5px solid var(--ink);display:inline-block}
  .contact{
    height:28px;border-radius:14px;font-weight:400;font-size:13.5px;text-transform:none;letter-spacing:.3px;
    justify-content:flex-start;padding-left:40px;
  }
  .contact svg{position:absolute;left:2px;top:2px}
</style>
</head>
<body>

<section class="card card-front" aria-label="Card front">
  <div class="abs brand"><span class="brand-dot"></span><span class="brand-name">Whitby's</span></div>
  <div class="rule" style="left:110px;width:420px;top:110px"></div>
  <div class="abs front-title">YARD &amp; GARDEN CENTER</div>
  <div class="abs front-and">AND</div>
  <div class="abs front-sub">YARD SERVICE LLC</div>
  <div class="rule" style="left:110px;width:420px;top:222px"></div>
  <div class="pill" style="left:100px;top:238px;width:210px">Landscaping</div>
  <div class="pill" style="left:110px;top:282px;width:210px">Snow Removal</div>
  <div class="pill" style="left:330px;top:238px;width:215px">Lawn Maintenance</div>
  <div class="pill" style="left:340px;top:282px;width:215px">Garden Center</div>
</section>

<section class="card card-back" aria-label="Card back">
  <div class="abs ghost" aria-hidden="true">Whitby's</div>
  <div class="abs person"><b>DESMOND</b> <span>WHITBY</span></div>
  <div class="rule" style="left:48px;width:120px;top:88px"></div>
  <div class="abs role">FOUNDER</div>

  <div class="pill service" style="left:372px;top:50px;width:228px">Landscaping
    <svg width="22" height="22" viewBox="0 0 22 22"><circle cx="11" cy="11" r="9.5" fill="none" stroke="#fff" stroke-width="2"/><path d="M6.5 11.5l3 3 6-7" fill="none" stroke="#fff" stroke-width="2.2"/></svg></div>
  <div class="pill service" style="left:372px;top:84px;width:228px">Snow Removal
    <svg width="22" height="22" viewBox="0 0 22 22"><circle cx="11" cy="11" r="9.5" fill="none" stroke="#fff" stroke-width="2"/><path d="M6.5 11.5l3 3 6-7" fill="none" stroke="#fff" stroke-width="2.2"/></svg></div>
  <div class="pill service" style="left:372px;top:118px;width:228px">Garden Center
    <svg width="22" height="22" viewBox="0 0 22 22"><circle cx="11" cy="11" r="9.5" fill="none" stroke="#fff" stroke-width="2"/><path d="M6.5 11.5l3 3 6-7" fill="none" stroke="#fff" stroke-width="2.2"/></svg></div>
  <div class="pill service" style="left:372px;top:152px;width:228px">Lawn Maintenance
    <svg width="22" height="22" viewBox="0 0 22 22"><circle cx="11" cy="11" r="9.5" fill="none" stroke="#fff" stroke-width="2"/><path d="M6.5 11.5l3 3 6-7" fill="none" stroke="#fff" stroke-width="2.2"/></svg></div>

  <div class="abs company">
    <div class="main">YARD &amp; GARDEN CENTER</div>
    <div class="and">AND</div>
    <div class="sub">YARD SERVICE LLC</div>
  </div>

  <div class="pill contact" style="left:40px;top:250px;width:180px">(555) 208-7316
    <svg width="24" height="24" viewBox="0 0 24 24"><circle cx="12" cy="12" r="11" fill="#fff" stroke="#3b5229" stroke-width="1.5"/><rect x="8.5" y="5.5" width="7" height="13" rx="1.2" fill="none" stroke="#3b5229" stroke-width="1.5"/><circle cx="12" cy="16" r=".9" fill="#3b5229"/></svg></div>
  <div class="pill contact" style="left:40px;top:284px;width:180px">(555) 391-6842
    <svg width="24" height="24" viewBox="0 0 24 24"><circle cx="12" cy="12" r="11" fill="#fff" stroke="#3b5229" stroke-width="1.5"/><path d="M8 6.5l2.2-.4 1.3 3-1.4 1.1a7 7 0 0 0 3.7 3.7l1.1-1.4 3 1.3-.4 2.2c-5.2.6-10.1-4.3-9.5-9.5z" fill="#3b5229"/></svg></div>
  <div class="pill contact" style="left:40px;top:318px;width:360px">Desmond@Whitbysyardandgarden.example
    <svg width="24" height="24" viewBox="0 0 24 24"><circle cx="12" cy="12" r="11" fill="#fff" stroke="#3b5229" stroke-width="1.5"/><rect x="6" y="8" width="12" height="8.5" rx="1" fill="#3b5229"/><path d="M6.5 8.5l5.5 4.2 5.5-4.2" fill="none" stroke="#fff" stroke-width="1.2"/></svg></div>
</section>

</body>
</html>
```